Business Card Design

We need a business card design for an existing business. Our main trading brand is www.brightquillsaver.co.uk

We attach various logo files - please use the version that will produce the sharpest image on the business card.

We are flexible about shape of card etc. Please think outside the box as to what goes on front and what goes on back of the card

We want to be able to amend the card (once the design has been agreed ) to add additional staff details, but the text to go on it will be generic

Details to go on card ( for the first generic one) are fairly minimal as we don't like cluttered business cards:-

Neil Cathcart
Managing Director

Mobile: 07841 258 407
Email: n.cathcart@brightquillsaver.co.uk

Industry/Entity Type

Business

```html
<!DOCTYPE html>
<html lang="en">
<head>
<meta charset="utf-8">
<title>Bright Quill Saver – Business Card</title>
<link href="https://fonts.googleapis.com/css2?family=Questrial&display=swap" rel="stylesheet">
<style>
  :root {
    --canvas-bg: #e9e6e1;
    --card-dark: #161718;
    --card-light: #ffffff;
    --brand-blue: #3f9fdc;
    --brand-sky: #8fcdf0;
    --ink: #1f2a33;
    --ink-soft: #3b4650;
    --shadow: rgba(0, 0, 0, 0.22);
  }
  * { box-sizing: border-box; margin: 0; padding: 0; }
  html, body {
    width: 1200px;
    height: 1024px;
    overflow: hidden;
    background: var(--canvas-bg);
    font-family: "Questrial", "Century Gothic", sans-serif;
  }
  .canvas {
    width: 1200px;
    height: 1024px;
    display: flex;
    flex-direction: column;
    align-items: center;
    justify-content: center;
    gap: 44px;
  }
  .card {
    position: relative;
    width: 700px;
    height: 453px;
    box-shadow: 0 10px 28px var(--shadow);
    overflow: hidden;
  }

  /* Front: dark card */
  .card--front { background: var(--card-dark); }
  .front__mark {
    position: absolute;
    right: 86px;
    top: 70px;
    width: 190px;
    height: 190px;
    border-radius: 50%;
    background: var(--brand-blue);
    opacity: 0.55;
  }
  .front__wordmark {
    position: absolute;
    left: 48px;
    bottom: 44px;
    font-size: 58px;
    letter-spacing: 0.5px;
    color: var(--brand-blue);
  }

  /* Back: white card */
  .card--back { background: var(--card-light); }
  .back__details {
    position: absolute;
    right: 46px;
    top: 46px;
    text-align: right;
  }
  .back__wordmark {
    font-size: 34px;
    color: var(--brand-blue);
    margin-bottom: 30px;
  }
  .back__name {
    font-size: 38px;
    color: var(--ink);
    line-height: 1.05;
  }
  .back__role {
    font-size: 19px;
    color: var(--brand-blue);
    margin-bottom: 30px;
  }
  .contact {
    list-style: none;
    font-size: 19px;
    color: var(--ink-soft);
    line-height: 1.55;
  }
  .contact__item {
    display: flex;
    justify-content: flex-end;
    align-items: center;
    gap: 10px;
  }
  .contact__icon { width: 18px; height: 18px; flex: none; }
  .address {
    margin-top: 14px;
    font-size: 19px;
    color: var(--ink);
    line-height: 1.4;
    font-style: normal;
  }
</style>
</head>
<body>
  <main class="canvas">
    <section class="card card--front" aria-label="Card front">
      <div class="front__mark"></div>
      <div class="front__wordmark">brightquillsaver.co.uk</div>
    </section>

    <section class="card card--back" aria-label="Card back">
      <div class="back__details">
        <div class="back__wordmark">brightquillsaver.co.uk</div>
        <h1 class="back__name">Neil Cathcart</h1>
        <p class="back__role">Managing Director</p>
        <ul class="contact">
          <li class="contact__item">07841 258 407
            <svg class="contact__icon" viewBox="0 0 18 18" aria-hidden="true">
              <rect x="5" y="1.5" width="8" height="15" rx="1.5" fill="none" stroke="var(--brand-blue)" stroke-width="1.6"/>
              <circle cx="9" cy="13.6" r="1" fill="var(--brand-blue)"/>
            </svg>
          </li>
          <li class="contact__item">n.cathcart@brightquillsaver.co.uk
            <svg class="contact__icon" viewBox="0 0 18 18" aria-hidden="true">
              <rect x="1.5" y="3.5" width="15" height="11" rx="1" fill="var(--ink)"/>
              <path d="M2 4l7 6 7-6" fill="none" stroke="#fff" stroke-width="1.3"/>
            </svg>
          </li>
          <li class="contact__item">www.brightquillsaver.co.uk
            <svg class="contact__icon" viewBox="0 0 18 18" aria-hidden="true">
              <circle cx="9" cy="9" r="7.2" fill="none" stroke="var(--brand-blue)" stroke-width="1.6"/>
              <ellipse cx="9" cy="9" rx="3" ry="7.2" fill="none" stroke="var(--brand-blue)" stroke-width="1.2"/>
              <path d="M2 9h14" stroke="var(--brand-blue)" stroke-width="1.2"/>
            </svg>
          </li>
        </ul>
        <address class="address">Harlow Court, 48 Fenwick Road, London<br>EC2A 4PL</address>
      </div>
    </section>
  </main>
</body>
</html>
```